Stationary for Beauty and Spa School

Create a business card, letterhead and envelopes (primarily #10 envelope with and without window and catalog envelope) for a beauty and wellness school in Miami, Fl. We offer 8 different programs of study and need an eye catching look. Looking for a combination of modern yet sophisticated. Nothing corporate or business looking. Would like to have a look and feel that is similar (or incorporates aspects) of a new website we will be launching in the next 30 days (screen shot attached.)

The final design should communicate style and elegance in a down to earth and friendly way. We strive to provide our students with quality education, friendly and amicable staff and experienced instructors.
Updates

Hello. FYI, in order to print an aesthetically appealing business card, we would like to print them (the business cards) using silk printing method, with spot UV coating (on some elements, maybe the logo, or depending on the design) and die cuts. Please think of this when preparing your design.

Only 1 day left, please submit your designs for selection. Thanks

Target Market(s)

Adults 18-49 years who are mostly interested in beauty and fashion. Need a youthful & modern look, yet sophisticated and elegant.

Industry/Entity Type

School

Colors
e34197
6b449b
add136
f79021

Requirements
Must have
• Similar look and feel as website (see attached screen shot)
Same look and feel of website (see attached screenshot)
Logo
Address: 5126 NW 14th Avenue. Miami, Fl 33157
Telephone: 305-914-3062
Fax: 786-552-4190
website/url: www.lumaroveacademy.edu
incorporate Photo of blonde model (attached)
Nice to have
• Tag line: "Beautify your future." Also, maybe two-sided business card. Would be nice if we could mention our programs (maybe in the back of the card). Below are the program offerings (names cannot be changed but order is irrelevant)... Cosmetology, Barber, Spa Therapy, Massage Therapy, Makeup Artistry, Skin Care, Manicure, Pedicure & Nail Extensions, Full Specialist.

A design with text plus a beautiful photo of a model is appealing. Attached to the files is a sample of a cover for a student handbook we have created. You should use the photo of the blonde model (attached) in your design. The original (quality) version of this stock photograph has been uploaded.

Also would be nice to request clients to follow us on facebook and instagram by including the icons.
Should not have
• A corporate or business look. We are a vocational school teaching beauty and spa programs and we like our advertising to have a look that resembles the industry. We do not want a very serious look or snobby feel.

```html
<!DOCTYPE html>
<html lang="en">
<head>
<meta charset="utf-8">
<title>Lumarove Academy – Business Card</title>
<link rel="stylesheet" href="https://fonts.googleapis.com/css2?family=Open+Sans:wght@300;400;600;700&display=swap">
<style>
  :root {
    --canvas: #fefbf3;
    --purple: #6e4397;
    --pink: #e84a95;
    --white: #ffffff;
    --photo-light: #f1e3d6;
    --photo-mid: #d9b9a2;
    --photo-deep: #8c6a5a;
  }
  * { margin: 0; padding: 0; box-sizing: border-box; }
  html, body { width: 1200px; height: 1000px; overflow: hidden; }
  body {
    background: var(--canvas);
    font-family: "Open Sans", Arial, sans-serif;
    color: var(--white);
    position: relative;
  }
  .card {
    position: absolute;
    top: 97px;
    width: 544px;
    height: 306px;
    overflow: hidden;
  }
  .card--front { left: 40px; background: var(--purple); }
  .card--back { left: 615px; background: var(--pink); }

  .front-art { position: absolute; inset: 0; }

  .holder {
    position: absolute;
    right: 26px;
    top: 30px;
    text-align: right;
  }
  .holder__name { font-size: 22px; font-weight: 600; line-height: 1.2; }
  .holder__role { font-size: 17px; font-weight: 300; line-height: 1.3; }

  .brand {
    position: absolute;
    right: 26px;
    bottom: 34px;
    font-size: 24px;
    font-weight: 600;
    color: var(--white);
    white-space: nowrap;
  }

  .back-head {
    height: 87px;
    display: flex;
    align-items: center;
    justify-content: space-between;
    padding: 0 43px 0 34px;
  }
  .back-head .brand-line { font-size: 24px; font-weight: 600; }
  .tagline { font-size: 22px; font-weight: 300; }

  .contact {
    height: 123px;
    background: var(--purple);
    text-align: center;
    padding-top: 13px;
    font-size: 20px;
    font-weight: 300;
    line-height: 25px;
  }
  .contact__web { font-weight: 600; }

  .programs {
    text-align: center;
    padding-top: 9px;
    font-size: 18px;
    font-weight: 300;
    line-height: 22.5px;
  }
</style>
</head>
<body>

  <section class="card card--front">
    <svg class="front-art" width="544" height="306" viewBox="0 0 544 306">
      <defs>
        <linearGradient id="portraitTone" x1="0" y1="0" x2="1" y2="1">
          <stop offset="0" stop-color="var(--photo-mid)"/>
          <stop offset="0.45" stop-color="var(--photo-light)"/>
          <stop offset="1" stop-color="var(--photo-deep)"/>
        </linearGradient>
      </defs>
      <path role="img" aria-label="Portrait photo of a blonde model with bold pink lips and smoky eye makeup"
            d="M0,0 H212 C292,55 332,175 322,306 H0 Z" fill="url(#portraitTone)"/>
      <path d="M212,0 C292,55 332,175 322,306" fill="none" stroke="var(--pink)" stroke-width="5"/>
    </svg>
    <div class="holder">
      <p class="holder__name">Name Surname</p>
      <p class="holder__role">position</p>
    </div>
    <p class="brand">Lumarove Academy</p>
  </section>

  <section class="card card--back">
    <header class="back-head">
      <p class="brand-line">Lumarove Academy</p>
      <p class="tagline">Beautify your future</p>
    </header>
    <div class="contact">
      <p>5126 NW 14th Avenue. Miami, Fl 33157</p>
      <p>Telephone: 305-914-3062</p>
      <p>Fax: 786-552-4190</p>
      <p class="contact__web">www.lumaroveacademy.edu</p>
    </div>
    <div class="programs">
      <p>Cosmetology &nbsp;|&nbsp; Barber &nbsp;|&nbsp; Spa Therapy &nbsp;&nbsp;|&nbsp; Skin Care</p>
      <p>Manicure &nbsp;|&nbsp; Massage Therapy &nbsp;|&nbsp; Makeup Artistry</p>
      <p>Pedicure &amp; Nail Extensions &nbsp;|&nbsp; Full Specialist</p>
    </div>
  </section>

</body>
</html>
```